ALL TYPES OF COMMERCIAL PLASTERING

TYPE OF BLOCK LETTERING WITH STAND OUT QUALITIES
WITH SOME TYPE OF LOGO
SOMETHING UNIQUE FOR THE BUILDING INDUSTRY.
QUALITY WORKMANSHIP
Updates

forgot to include my mobile phone number on my brief. could you add it to your design please MOBILE PH 0418 695 031

please let me make this quite clear ,the company name is northgate linings and Fitouts PTY LTD. THE TYPE OF WORK WE WILL BE DOING IS COMMERCIAL PLASTERING.

Industry/Entity Type

Industry

Contact Information for Business Card

northgate linings and fitouts P/L
martin corbell p.o.box 42 wendouree 3355 email address northgatelinings@mailbox-example.com
ABN 51 847 213 906 COMMERCIAL PLASTERING

```html
<!DOCTYPE html>
<html lang="en">
<head>
<meta charset="utf-8">
<title>Northgate Linings and Fitouts – Business Card</title>
<link rel="stylesheet" href="https://fonts.googleapis.com/css2?family=Oswald:wght@500;700&family=Arimo:wght@400;700&display=swap">
<style>
  :root {
    --backdrop: #1e1e1e;
    --plaster-light: #f1e7da;
    --plaster-mid: #e6d6c2;
    --plaster-deep: #d6bd9b;
    --ink-dark: #464644;
    --ink-text: #3a3a38;
    --accent-tan: #b3956a;
  }
  * { margin: 0; padding: 0; box-sizing: border-box; }
  html, body {
    width: 1200px;
    height: 800px;
    overflow: hidden;
    background: var(--backdrop);
  }
  .canvas {
    position: relative;
    width: 1200px;
    height: 800px;
  }
  .business-card {
    position: absolute;
    left: 100px;
    top: 100px;
    width: 1000px;
    height: 600px;
    overflow: hidden;
    background: var(--plaster-light);
  }
  .plaster-photo {
    position: absolute;
    inset: 0;
    background:
      radial-gradient(ellipse 55% 45% at 18% 85%, var(--plaster-deep) 0%, rgba(214,189,155,0) 100%),
      linear-gradient(160deg, var(--plaster-light) 0%, var(--plaster-mid) 60%, var(--plaster-deep) 100%);
  }
  .service-title {
    position: absolute;
    right: 78px;
    top: 66px;
    font-family: "Oswald", sans-serif;
    font-weight: 700;
    font-size: 82px;
    line-height: 1;
    letter-spacing: 2px;
    color: var(--ink-dark);
    white-space: nowrap;
  }
  .company-name {
    position: absolute;
    left: 0;
    width: 1000px;
    text-align: center;
    top: 170px;
    padding-left: 0;
    font-family: "Oswald", sans-serif;
    font-weight: 700;
    font-size: 28px;
    letter-spacing: 1.5px;
    color: var(--accent-tan);
    text-transform: uppercase;
  }
  .contact-block {
    position: absolute;
    right: 78px;
    top: 322px;
    text-align: right;
  }
  .contact-name {
    font-family: "Oswald", sans-serif;
    font-weight: 500;
    font-size: 50px;
    line-height: 1.1;
    font-variant: small-caps;
    letter-spacing: 1px;
    color: var(--accent-tan);
    margin-bottom: 30px;
  }
  .contact-address {
    font-family: "Arimo", sans-serif;
    font-size: 26px;
    color: var(--ink-text);
    margin-bottom: 28px;
  }
  .contact-phone {
    font-family: "Arimo", sans-serif;
    font-weight: 700;
    font-size: 36px;
    color: var(--ink-text);
    line-height: 1.1;
  }
  .contact-email {
    font-family: "Arimo", sans-serif;
    font-weight: 700;
    font-size: 27px;
    color: var(--ink-text);
    margin-top: 2px;
  }
  .abn {
    position: absolute;
    left: 160px;
    top: 530px;
    font-family: "Arimo", sans-serif;
    font-size: 18px;
    color: var(--ink-text);
  }
</style>
</head>
<body>
  <main class="canvas">
    <section class="business-card">
      <div class="plaster-photo" role="img" aria-label="Photo of a hand spreading plaster across a wall with a trowel"></div>
      <h1 class="service-title">COMMERCIAL PLASTERING</h1>
      <p class="company-name">Northgate linings and fitouts P/L</p>
      <div class="contact-block">
        <p class="contact-name">Martin Corbell</p>
        <p class="contact-address">P.O. Box 42 Wendouree 3355</p>
        <p class="contact-phone">0418 695 031</p>
        <p class="contact-email">northgatelinings@mailbox-example.com</p>
      </div>
      <p class="abn">ABN 51 847 213 906</p>
    </section>
  </main>
</body>
</html>
```